NAT stands for Nell and Tova - teenager girls that will provide makeup and photography services for proms, weddings, graduations and other special events. The design should be bright and cheery and have the teenage audience it will be directed to in mind. I want the word "NAT" to be a part of the postcard and be essentially a logo by itself with the names somewhere under it.

Target Market(s)

Teenagers

Industry/Entity Type

Makeup

Requirements
Must have
• The Word "NAT" as the logo for the make up and photography services with the girls name in smaller font somewhere to identify what "NAT" stands for.
Nice to have
• I like circles and bright colors. I like tie dye too. There should be room to put a couple photos of their work on the postcard.
Should not have
• No address will be proved

```html
<!DOCTYPE html>
<html lang="en">
<head>
<meta charset="utf-8">
<title>NAT makeup and photography – postcard</title>
<link rel="stylesheet" href="https://fonts.googleapis.com/css2?family=Great+Vibes&family=Lora:ital,wght@0,400;1,400&display=swap">
<style>
  :root {
    --board: #2d2d2d;
    --blush: #fbeef2;
    --blush-deep: #f6dfe7;
    --lavender: #9a6cb5;
    --lavender-dark: #8a5aa6;
    --magenta: #a8439f;
    --magenta-light: #c86cc0;
    --ink: #1c1c1c;
    --white: #ffffff;
    --photo-dark: #5b4a4a;
    --photo-light: #d8b6a4;
  }
  * { margin: 0; padding: 0; box-sizing: border-box; }
  html, body { width: 1200px; height: 1200px; overflow: hidden; }
  body { background: var(--board); font-family: "Lora", Georgia, serif; position: relative; }

  .card { position: absolute; overflow: hidden; }
  .card-front {
    left: 36px; top: 38px; width: 720px; height: 553px;
    background: radial-gradient(ellipse at 30% 30%, var(--white) 0%, var(--blush) 55%, var(--blush-deep) 100%);
  }
  .card-back { left: 412px; top: 618px; width: 719px; height: 553px; background: var(--white); }

  .abs { position: absolute; }
  .italic { font-style: italic; }

  .brand-mark { left: 20px; top: 18px; font-family: "Great Vibes", cursive; font-size: 86px; line-height: 1; color: var(--magenta); }
  .brand-tagline { left: 17px; top: 110px; font-size: 18px; font-style: italic; color: #333; }
  .intro { left: 22px; top: 155px; width: 280px; font-size: 16px; line-height: 20px; font-style: italic; color: var(--ink); }
  .intro .names { color: var(--magenta); }
  .services-title { left: 22px; top: 254px; font-size: 21px; font-style: italic; color: var(--magenta-light); }
  .service-list { left: 24px; top: 298px; list-style: none; font-size: 16px; font-style: italic; color: var(--ink); }
  .service-list li { height: 36px; display: flex; gap: 6px; align-items: flex-start; }
  .service-list svg { margin-top: 6px; }

  .front-band { left: 0; top: 0; width: 720px; height: 553px; }

  .photo-circle { border-radius: 50%; border: 7px solid var(--magenta); }
  .photo-main { left: 293px; top: 22px; width: 356px; height: 356px;
    background: radial-gradient(circle at 50% 45%, var(--photo-light) 0%, #9e7f72 45%, var(--photo-dark) 100%); }
  .photo-second { left: 478px; top: 177px; width: 234px; height: 234px;
    background: radial-gradient(circle at 45% 45%, #e9cfc0 0%, #b4826a 60%, #7a5446 100%); }

  .offer-badge { left: 246px; top: 358px; width: 182px; height: 182px; border-radius: 50%;
    background: radial-gradient(circle at 40% 30%, var(--magenta-light) 0%, var(--magenta) 70%, #8c3386 100%);
    color: var(--white); font-style: italic; text-align: center;
    display: flex; flex-direction: column; justify-content: center; }
  .offer-text { transform: rotate(-24deg); line-height: 1.1; }
  .offer-text .o1 { font-size: 21px; }
  .offer-text .o2 { font-size: 27px; }
  .offer-text .o3 { font-size: 16px; }

  .appointment { left: 474px; top: 470px; font-size: 21px; font-style: italic; color: var(--white); }
  .phone-big { left: 466px; top: 498px; font-size: 35px; font-style: italic; color: var(--white); }

  .back-panel { left: 0; top: 0; width: 719px; height: 553px; }
  .price-title { left: 29px; top: 28px; font-size: 26px; font-style: italic; color: var(--white); }
  .price-group { left: 30px; font-size: 20px; font-style: italic; color: var(--white); }
  .price-rows { left: 30px; list-style: none; font-size: 16px; font-style: italic; color: var(--white); }
  .price-rows li { height: 28.7px; }
  .price-note { left: 15px; top: 452px; width: 270px; font-size: 15px; line-height: 18px; font-style: italic; color: var(--white); }

  .sender-name { left: 342px; top: 40px; font-family: "Great Vibes", cursive; font-size: 30px; color: var(--magenta); line-height: 1; }
  .sender-tag { left: 342px; top: 74px; font-size: 10px; font-style: italic; color: #333; }
  .sender-contact { left: 344px; top: 95px; font-size: 10.5px; line-height: 17px; color: var(--ink); }
  .stamp-box { left: 530px; top: 44px; width: 122px; height: 123px; border: 2px solid #111; }
</style>
</head>
<body>

<section class="card card-front">
  <svg class="abs front-band" viewBox="0 0 720 553" aria-hidden="true">
    <path d="M0 470 C150 520 300 470 430 450 C560 430 640 420 720 440 L720 553 L0 553 Z" fill="var(--lavender)"/>
    <path d="M0 478 C150 528 300 478 430 458 C560 438 640 428 720 448" fill="none" stroke="var(--white)" stroke-width="3"/>
    <path d="M0 486 C150 536 300 486 430 466 C560 446 640 436 720 456" fill="none" stroke="var(--magenta)" stroke-width="4"/>
    <path d="M0 496 C150 546 300 496 430 476 C560 456 640 446 720 466" fill="none" stroke="var(--white)" stroke-width="1.5" opacity="0.7"/>
  </svg>

  <div class="abs brand-mark">NAT</div>
  <div class="abs brand-tagline">makeup and photography</div>
  <p class="abs intro"><span class="names">Nell and Tova</span> are freelance Hair, Make-up &amp; Photography, specializing in proms, weddings, graduations and other special events</p>
  <h2 class="abs services-title">List Of Services We Offer</h2>
  <ul class="abs service-list">
    <li><svg width="10" height="9" viewBox="0 0 10 9"><path d="M1 5 L4 8 L9 1" fill="none" stroke="#222" stroke-width="2"/></svg>Lorem ipsum dolor sit amet</li>
    <li><svg width="10" height="9" viewBox="0 0 10 9"><path d="M1 5 L4 8 L9 1" fill="none" stroke="#222" stroke-width="2"/></svg>Consectetuer adipiscing elit</li>
    <li><svg width="10" height="9" viewBox="0 0 10 9"><path d="M1 5 L4 8 L9 1" fill="none" stroke="#222" stroke-width="2"/></svg>Sed diam nonummy nibh</li>
    <li><svg width="10" height="9" viewBox="0 0 10 9"><path d="M1 5 L4 8 L9 1" fill="none" stroke="#222" stroke-width="2"/></svg>Tncidunt ut laoreet</li>
    <li><svg width="10" height="9" viewBox="0 0 10 9"><path d="M1 5 L4 8 L9 1" fill="none" stroke="#222" stroke-width="2"/></svg>Sliquam erat volutpat.</li>
  </ul>

  <div class="abs photo-circle photo-main" role="img" aria-label="Photo of a bride with a veil and finished makeup"></div>
  <div class="abs photo-circle photo-second" role="img" aria-label="Photo of a bride with styled hair and a hair piece"></div>

  <div class="abs offer-badge">
    <div class="offer-text">
      <div class="o1">Special Offer</div>
      <div class="o2">Get $30 off</div>
      <div class="o3">some offer text<br>goes here</div>
    </div>
  </div>

  <div class="abs appointment">For Appointment Call</div>
  <div class="abs phone-big">555-014-2287</div>
</section>

<section class="card card-back">
  <svg class="abs back-panel" viewBox="0 0 719 553" aria-hidden="true">
    <path d="M0 0 L288 0 C340 110 350 260 320 380 C300 460 270 520 250 553 L0 553 Z" fill="var(--lavender)"/>
    <path d="M288 0 C340 110 350 260 320 380 C300 460 270 520 250 553" fill="none" stroke="var(--white)" stroke-width="3"/>
    <path d="M298 0 C350 110 360 260 330 380 C310 460 280 520 260 553" fill="none" stroke="var(--magenta)" stroke-width="5"/>
  </svg>

  <h2 class="abs price-title">Services Price List</h2>
  <h3 class="abs price-group" style="top:86px;font-weight:400">Hair and Beauty</h3>
  <ul class="abs price-rows" style="top:124px">
    <li>Service.............................Cost</li>
    <li>Service.............................Cost</li>
    <li>Service.............................Cost</li>
    <li>Service.............................Cost</li>
    <li>Service.............................Cost</li>
    <li>Service.............................Cost</li>
  </ul>
  <h3 class="abs price-group" style="top:311px;font-weight:400">Photography</h3>
  <ul class="abs price-rows" style="top:349px">
    <li>1 Hour Photography...............Cost</li>
    <li>2 Hour Photography...............Cost</li>
    <li>3Hour Photography...............Cost</li>
  </ul>
  <p class="abs price-note">You will receive a minimum of 80 high resolution photos in digital Jpeg format for every hour of photography, beautifully presented on a USB stick</p>

  <div class="abs sender-name">Nell and Tova</div>
  <div class="abs sender-tag">makeup and photography services</div>
  <div class="abs sender-contact">555-014-2287<br>natmakeupandphoto@example.com</div>
  <div class="abs stamp-box"></div>
</section>

</body>
</html>
```